Leap! Maximizing the Transfer of a Company to Seasoned Buyers

We are a private equity firm, and the partners wrote this book to help business owners understand the process for selling their business. We need a cover for the book, and our current thinking is a picture of a person (or just the leg/foot w/business shoe) walking out a door, representing our title "Leap!"
Business owners will benefit from learning what professional investors, like private equity firms, are looking for and how the process is likely to unfold. Business owners will also learn how to prepare their company and themselves for this process.

Target Market(s)

Small to medium sized business owners

Font styles to use
Serif

Colors
3277b5
3276b5
85acd3
cfdeed

Requirements
Must have
• a professional look and feel that will attract business owners and a compelling call to action for those business owners considering a sale of their business
Nice to have
• Leverage the same color blue and possibly logo from Birch Hollow Capital, which can be seen here - https://birchhollowcap.example/
Should not have
• humor/quirkiness/schtick

```html
<!DOCTYPE html>
<html lang="en">
<head>
<meta charset="utf-8">
<title>Leap! Maximizing the Transfer of a Company to Seasoned Buyers</title>
<link rel="stylesheet" href="https://fonts.googleapis.com/css2?family=Archivo:wdth,wght@125,800&family=Oswald:wght@400;700&display=swap">
<style>
  :root {
    --paper: #ffffff;
    --navy: #1e3461;
    --accent-red: #e8121b;
    --suit-dark: #1c1d22;
    --suit-mid: #3a3b42;
  }
  * { margin: 0; padding: 0; box-sizing: border-box; }
  html, body { width: 800px; height: 1200px; overflow: hidden; background: var(--paper); }
  .cover {
    position: relative;
    width: 800px;
    height: 1200px;
    background: var(--paper);
    overflow: hidden;
  }
  .cover-photo {
    position: absolute;
    left: 0;
    top: 0;
    width: 584px;
    height: 792px;
    background:
      radial-gradient(ellipse 60% 70% at 35% 30%, var(--suit-mid) 0%, var(--suit-dark) 45%, rgba(28,29,34,0) 75%),
      linear-gradient(180deg, rgba(255,255,255,0) 70%, var(--paper) 100%);
  }
  .publisher {
    position: absolute;
    left: 428px;
    top: 114px;
    display: flex;
    align-items: center;
    gap: 12px;
  }
  .publisher-mark {
    width: 38px;
    height: 38px;
    background: var(--navy);
  }
  .publisher-name {
    font-family: "Oswald", sans-serif;
    font-weight: 400;
    font-size: 34px;
    line-height: 1;
    color: var(--navy);
    white-space: nowrap;
  }
  .title-block {
    position: absolute;
    left: 0;
    top: 768px;
    width: 800px;
    text-align: center;
  }
  .title-accent {
    position: absolute;
    left: 478px;
    top: 0;
    width: 28px;
    height: 32px;
  }
  .title {
    position: absolute;
    left: 0;
    top: 34px;
    width: 800px;
    font-family: "Archivo", sans-serif;
    font-stretch: 125%;
    font-weight: 800;
    font-size: 146px;
    line-height: 1;
    letter-spacing: 0.14em;
    padding-left: 0.14em;
    color: var(--navy);
  }
  .subtitle {
    position: absolute;
    left: 0;
    top: 970px;
    width: 800px;
    text-align: center;
    font-family: "Oswald", sans-serif;
    font-weight: 700;
    font-size: 31px;
    line-height: 1.35;
    color: var(--navy);
  }
</style>
</head>
<body>
  <main class="cover">
    <div class="cover-photo" role="img" aria-label="Photograph of legs in a dark pinstripe suit and black leather shoes, one foot stepping forward with its sole raised"></div>

    <div class="publisher">
      <span class="publisher-mark"></span>
      <span class="publisher-name">Birch Hollow Capital</span>
    </div>

    <div class="title-block">
      <svg class="title-accent" viewBox="0 0 28 32" aria-hidden="true">
        <polygon points="0,0 28,16 0,32" fill="var(--accent-red)"/>
      </svg>
      <h1 class="title">LEAP</h1>
    </div>

    <p class="subtitle">Maximizing the Transfer of a Company<br>to Seasoned Buyers</p>
  </main>
</body>
</html>
```